Ferncrest Dental, LLC business card project

Business card to be designed with current logo.
Dental office- please keep design of card that looks clean and professional.
Please include the following info:
Ferncrest Dental, LLC
Dr. Lorna Pettigrew
2871 Marlowe Street
Bethlehem, PA 18093
610-555-0193
ferncrestdental.office@examplemail.test
Hello everyone-
Reason: Just got back from overseas- will look at all designs and provide feedback. Thank you!
Reason: Polling my friends for the final selection-
thank you to all those that participated- so many talented designers!

```html
<!DOCTYPE html>
<html lang="en">
<head>
<meta charset="utf-8">
<title>Ferncrest Dental, LLC – Business Card</title>
<link href="https://fonts.googleapis.com/css2?family=Questrial&family=Mulish:wght@700&display=swap" rel="stylesheet">
<style>
  :root {
    --backdrop: #dcdcdc;
    --card: #ffffff;
    --lime: #a6c93c;
    --leaf: #8dbb3e;
    --forest: #5e9a2c;
    --shadow: rgba(0, 0, 0, 0.18);
  }
  html, body {
    margin: 0;
    padding: 0;
    width: 1200px;
    height: 602px;
    overflow: hidden;
    background: var(--backdrop);
  }
  .stage {
    position: relative;
    width: 1200px;
    height: 602px;
  }
  .card {
    position: absolute;
    top: 155px;
    width: 425px;
    height: 275px;
    background: var(--card);
    box-shadow: 0 2px 6px var(--shadow);
  }
  .card--front { left: 85px; }
  .card--back { left: 690px; }

  .brand {
    display: flex;
    align-items: center;
    gap: 8px;
    font-family: "Questrial", sans-serif;
    color: var(--leaf);
    white-space: nowrap;
  }
  .brand__dot {
    border-radius: 50%;
    background: var(--leaf);
    flex: none;
  }
  .card--front .brand {
    position: absolute;
    left: 0;
    right: 0;
    top: 120px;
    justify-content: center;
    font-size: 26px;
  }
  .card--front .brand__dot { width: 16px; height: 16px; }

  .card--back .brand {
    position: absolute;
    right: 25px;
    top: 27px;
    font-size: 17px;
    gap: 6px;
  }
  .card--back .brand__dot { width: 10px; height: 10px; }

  .holder {
    position: absolute;
    left: 25px;
    top: 105px;
  }
  .holder__name {
    margin: 0;
    font-family: "Mulish", sans-serif;
    font-weight: 700;
    font-size: 17px;
    color: var(--forest);
    letter-spacing: 0.2px;
  }
  .holder__swoosh {
    display: block;
    margin-top: 1px;
    margin-left: -2px;
  }

  .contact {
    position: absolute;
    right: 25px;
    top: 164px;
    margin: 0;
    text-align: right;
    font-family: "Questrial", sans-serif;
    font-style: normal;
    font-size: 14.5px;
    line-height: 17.6px;
    color: var(--lime);
  }
  .contact__company {
    font-family: "Mulish", sans-serif;
    font-weight: 700;
  }
  .contact__label {
    font-family: "Mulish", sans-serif;
    font-weight: 700;
    color: var(--forest);
  }
</style>
</head>
<body>
<main class="stage">
  <section class="card card--front" aria-label="Card front">
    <div class="brand">
      <span class="brand__dot"></span>
      <span class="brand__name">Ferncrest Dental, LLC</span>
    </div>
  </section>

  <section class="card card--back" aria-label="Card back">
    <div class="brand">
      <span class="brand__dot"></span>
      <span class="brand__name">Ferncrest Dental, LLC</span>
    </div>

    <div class="holder">
      <p class="holder__name">Dr. Lorna Pettigrew</p>
      <svg class="holder__swoosh" width="165" height="8" viewBox="0 0 165 8" aria-hidden="true">
        <path d="M0 7 Q 80 -1 165 4 Q 80 2 0 7 Z" fill="var(--lime)"/>
      </svg>
    </div>

    <address class="contact">
      <span class="contact__company">Ferncrest Dental, LLC</span><br>
      2871 Marlowe Street<br>
      Bethlehem, PA 18093<br>
      <span class="contact__label">t.</span> 610-555-0193<br>
      <span class="contact__label">e.</span> ferncrestdental.office@examplemail.test
    </address>
  </section>
</main>
</body>
</html>
```